Bref créative
Velvet Larder Business Cards
Logo has already been created!!
Bright & Fun-filled
Pete Hargrove
Owner
487 Cedar Ave.
Mapleton, IL 60605
wxyz@mailbrook.net
www.myvelvetlarder.com
We were very very satisfied during our logo design contest. Lot of creative minds here and that brings me back again for our business cards! Here is a link to our prior project -
http://orders.brandcraftforge.com/contests/project-velvet-larder-pup
We are young and will be setting up in urban area. We would like this factor to reflect in our business cards. We found sample business cards that we like on web -
http://vorteksketch.net/inspirations/60-most-beautiful-and-creative-business-cards-design/
We are still deciding on color scheme so please feel free to use different pallet/scheme while altering business logo.
Should include a space for facebook and twitter icon and id as well. Use VLSocialPage and VLChirpFeed as a dummy ids.
We are thinking that back of the business card would cover entire logo as a whole along with the website and/or tagline -
"There are local grocery stores and there is the Velvet Larder.
Experience the grocery shopping a Velvet Way!"

```html
<!DOCTYPE html>
<html lang="en">
<head>
<meta charset="utf-8">
<title>Velvet Larder Business Cards</title>
<link href="https://fonts.googleapis.com/css2?family=Roboto:wght@400;700;900&family=Varela+Round&display=swap" rel="stylesheet">
<style>
  :root {
    --page: #ececea;
    --white: #ffffff;
    --green-dark: #1d561b; --green: #2f7d2b; --green-light: #74b53c;
    --teal-dark: #15838b; --teal: #2cb4bc; --teal-light: #7fdadc;
    --brown-dark: #6e4a12; --brown: #a57726; --brown-light: #d2a648;
    --ink-teal: #0d3f44;
  }
  * { box-sizing: border-box; margin: 0; padding: 0; }
  html, body { width: 1200px; height: 1027px; overflow: hidden; }
  body { background: var(--page); font-family: "Roboto", Arial, sans-serif; position: relative; }

  .card { position: absolute; width: 270px; height: 470px; overflow: hidden; color: var(--white);
          box-shadow: 0 6px 18px rgba(0,0,0,.22); }
  .card.green { --dk: var(--green-dark); --md: var(--green); --lt: var(--green-light); --name: var(--white); }
  .card.teal  { --dk: var(--teal-dark);  --md: var(--teal);  --lt: var(--teal-light);  --name: var(--ink-teal); }
  .card.brown { --dk: var(--brown-dark); --md: var(--brown); --lt: var(--brown-light); --name: var(--white); }

  .row-front .card { top: 30px; }
  .row-back .card { top: 527px; }
  .col-1 { left: 120px; } .col-2 { left: 465px; } .col-3 { left: 810px; }

  /* front */
  .front { background: linear-gradient(180deg, var(--md) 0%, var(--lt) 55%, var(--md) 100%); }
  .front .top-band { position: absolute; left: 0; top: 0; width: 100%; height: 62px; background: var(--dk); }
  .front .tab { position: absolute; left: 0; top: 0; width: 26px; height: 26px; background: var(--lt); }
  .front .name { position: absolute; top: 78px; width: 100%; text-align: center; font-weight: 900;
                 font-size: 27px; color: var(--name); }
  .front .role { position: absolute; top: 114px; width: 100%; text-align: center; font-weight: 700;
                 font-size: 14px; color: var(--name); }
  .teal .rule { position: absolute; top: 134px; left: 30px; width: 210px; height: 2px; background: var(--ink-teal); }
  .front .wordmark { position: absolute; top: 178px; width: 100%; text-align: center;
                     font-family: "Varela Round", Arial, sans-serif; font-size: 30px; line-height: 30px; color: var(--white); }
  .front .area { position: absolute; top: 250px; width: 100%; text-align: center; font-size: 7px;
                 letter-spacing: 1.5px; color: var(--white); }
  .front .swoosh { position: absolute; left: 0; bottom: 0; width: 270px; height: 170px; }
  .front .contact { position: absolute; bottom: 26px; left: 0; width: 100%; display: flex;
                    justify-content: space-between; padding: 0 14px; font-size: 8px; line-height: 11px; }
  .front .contact b { display: block; font-weight: 700; }

  /* back */
  .back { background: linear-gradient(160deg, var(--lt) 0%, var(--md) 45%, var(--dk) 100%); }
  .back .tagline { position: absolute; top: 26px; left: 14px; width: 200px; font-size: 10px; line-height: 13px;
                   font-weight: 700; text-align: center; transform: rotate(-12deg); }
  .back .wordmark { position: absolute; top: 180px; width: 100%; text-align: center;
                    font-family: "Varela Round", Arial, sans-serif; font-size: 48px; line-height: 50px; }
  .back .area { position: absolute; top: 300px; width: 100%; text-align: center; font-size: 12px;
                letter-spacing: 3px; font-weight: 700; }
  .back .site { position: absolute; top: 322px; width: 100%; text-align: center; font-size: 12px; font-weight: 700; }
  .back .follow { position: absolute; bottom: 18px; left: 14px; right: 14px; display: flex; align-items: center;
                  gap: 8px; font-size: 8px; }
  .back .follow .id { display: flex; align-items: center; gap: 4px; }
  .back .follow .dot { width: 14px; height: 14px; background: var(--white); border-radius: 2px; }
</style>
</head>
<body>
  <section class="row-front">
    <article class="card front green col-1">
      <div class="top-band"></div><div class="tab"></div>
      <h1 class="name">Pete Hargrove</h1><p class="role">Owner</p>
      <p class="wordmark">velvet<br>larder</p><p class="area">NORTH END OF MAPLETON</p>
      <svg class="swoosh" viewBox="0 0 270 170"><path d="M0 60 Q135 0 270 50 V170 H0Z" fill="var(--dk)" opacity=".55"/><path d="M0 80 Q135 25 270 70 V170 H0Z" fill="var(--dk)"/></svg>
      <div class="contact"><span><b>Address</b>487 Cedar Ave.<br>Mapleton, IL</span><span><b>Cell</b>000-000-0000</span><span><b>Phone</b>000-000-0000</span></div>
    </article>
    <article class="card front teal col-2">
      <div class="top-band"></div><div class="tab"></div>
      <h1 class="name">Pete Hargrove</h1><p class="role">Owner</p><div class="rule"></div>
      <p class="wordmark">velvet<br>larder</p><p class="area">NORTH END OF MAPLETON</p>
      <svg class="swoosh" viewBox="0 0 270 170"><path d="M0 60 Q135 0 270 50 V170 H0Z" fill="var(--dk)" opacity=".55"/><path d="M0 80 Q135 25 270 70 V170 H0Z" fill="var(--dk)"/></svg>
      <div class="contact"><span><b>Address</b>487 Cedar Ave.<br>Mapleton, IL</span><span><b>Cell</b>000-000-0000</span><span><b>Phone</b>000-000-0000</span></div>
    </article>
    <article class="card front brown col-3">
      <div class="top-band"></div><div class="tab"></div>
      <h1 class="name">Pete Hargrove</h1><p class="role">Owner</p>
      <p class="wordmark">velvet<br>larder</p><p class="area">NORTH END OF MAPLETON</p>
      <svg class="swoosh" viewBox="0 0 270 170"><path d="M0 60 Q135 0 270 50 V170 H0Z" fill="var(--dk)" opacity=".55"/><path d="M0 80 Q135 25 270 70 V170 H0Z" fill="var(--dk)"/></svg>
      <div class="contact"><span><b>Address</b>487 Cedar Ave.<br>Mapleton, IL</span><span><b>Cell</b>000-000-0000</span><span><b>Phone</b>000-000-0000</span></div>
    </article>
  </section>

  <section class="row-back">
    <article class="card back green col-1">
      <p class="tagline">"There are local grocery stores and there is the Velvet Larder. Experience the grocery shopping a Velvet Way!"</p>
      <p class="wordmark">velvet<br>larder</p>
      <p class="area">NORTH END OF MAPLETON</p><p class="site">www.myvelvetlarder.com</p>
      <div class="follow"><span>follow us at</span><span class="id"><i class="dot"></i>VLSocialPage</span><span class="id"><i class="dot"></i>VLChirpFeed</span></div>
    </article>
    <article class="card back teal col-2">
      <p class="tagline">"There are local grocery stores and there is the Velvet Larder. Experience the grocery shopping a Velvet Way!"</p>
      <p class="wordmark">velvet<br>larder</p>
      <p class="area">NORTH END OF MAPLETON</p><p class="site">www.myvelvetlarder.com</p>
      <div class="follow"><span>follow us at</span><span class="id"><i class="dot"></i>VLSocialPage</span><span class="id"><i class="dot"></i>VLChirpFeed</span></div>
    </article>
    <article class="card back brown col-3">
      <p class="tagline">"There are local grocery stores and there is the Velvet Larder. Experience the grocery shopping a Velvet Way!"</p>
      <p class="wordmark">velvet<br>larder</p>
      <p class="area">NORTH END OF MAPLETON</p><p class="site">www.myvelvetlarder.com</p>
      <div class="follow"><span>follow us at</span><span class="id"><i class="dot"></i>VLSocialPage</span><span class="id"><i class="dot"></i>VLChirpFeed</span></div>
    </article>
  </section>
</body>
</html>
```